mapleridgegroup Business Card Design

Business card with logo design for mapleridgegroup. We are a group of professional project managers based on the Pareto Principle that 80% of the work is done by 20% of the people. I have a makeshift logo that uses a pi chart with 30% and 20% and the 20% pie slice is set slightly out and up. Have played around with a teal and orange colour scheme.

Industry/Entity Type

Business

Contact Information for Business Card

Gareth Pembroke
Director
mapleridgegroup

0452 803716

```html
<!DOCTYPE html>
<html lang="en">
<head>
<meta charset="utf-8">
<title>mapleridgegroup Business Card</title>
<link rel="stylesheet" href="https://fonts.googleapis.com/css2?family=Exo+2:wght@400;600;700&display=swap">
<style>
  :root {
    --backdrop: #d9d9d9;
    --card: #ffffff;
    --orange-deep: #e5503a;
    --orange-light: #f08d55;
    --teal: #2b9a9c;
    --ink: #3a3a3a;
    --ink-soft: #555555;
    --on-orange: #ffffff;
  }
  * { margin: 0; padding: 0; box-sizing: border-box; }
  html, body { width: 1200px; height: 949px; overflow: hidden; }
  body {
    background: var(--backdrop);
    font-family: "Exo 2", sans-serif;
    position: relative;
  }
  .card {
    position: absolute;
    left: 290px;
    width: 620px;
    height: 354px;
    border-radius: 22px;
    background: var(--card);
    overflow: hidden;
    box-shadow: 0 10px 28px rgba(0,0,0,0.18);
  }
  .card--front { top: 70px; }
  .card--back { top: 500px; }

  /* Front */
  .brand {
    position: absolute;
    inset: 0;
    display: flex;
    align-items: center;
    justify-content: center;
    gap: 14px;
  }
  .brand__dot {
    width: 34px; height: 34px;
    border-radius: 50%;
    background: var(--teal);
  }
  .brand__name {
    font-size: 34px;
    font-weight: 600;
    color: var(--orange-deep);
    letter-spacing: 0.5px;
  }

  /* Back */
  .back-art { position: absolute; inset: 0; }
  .text { position: absolute; white-space: nowrap; }
  .holder__name {
    left: 36px; top: 72px;
    font-size: 22px; font-weight: 700;
    color: var(--ink); letter-spacing: 1px;
  }
  .holder__role {
    left: 38px; top: 100px;
    font-size: 11px; font-weight: 600;
    color: var(--ink-soft); letter-spacing: 1px;
  }
  .address {
    left: 290px; top: 72px;
    font-size: 16px; font-weight: 600;
    color: var(--ink); line-height: 22px;
  }
  .phone {
    left: 480px; top: 170px;
    font-size: 18px; font-weight: 600;
    color: var(--ink); line-height: 23px; letter-spacing: 1px;
  }
  .web {
    left: 40px; top: 208px;
    font-size: 15px; color: var(--on-orange); line-height: 22px;
  }
  .social {
    left: 340px;
    font-size: 15px; color: var(--on-orange);
  }
  .social--one { top: 250px; }
  .social--two { top: 288px; }
  .social--three { top: 326px; }
</style>
</head>
<body>

<section class="card card--front" aria-label="Card front">
  <div class="brand">
    <span class="brand__dot"></span>
    <span class="brand__name">mapleridgegroup</span>
  </div>
</section>

<section class="card card--back" aria-label="Card back">
  <svg class="back-art" width="620" height="354" viewBox="0 0 620 354">
    <defs>
      <radialGradient id="bandFill" cx="45%" cy="45%" r="70%">
        <stop offset="0" stop-color="var(--orange-light)"/>
        <stop offset="1" stop-color="var(--orange-deep)"/>
      </radialGradient>
    </defs>
    <path class="band" d="M0 128 H440 V238 H620 V354 H0 Z" fill="url(#bandFill)"/>

    <!-- person icon -->
    <g class="icon icon--person">
      <circle cx="120" cy="38" r="18" fill="var(--teal)"/>
      <circle cx="120" cy="33" r="5" fill="#fff"/>
      <path d="M110 47 a10 8 0 0 1 20 0 Z" fill="#fff"/>
    </g>
    <!-- pin icon -->
    <g class="icon icon--pin">
      <circle cx="350" cy="42" r="18" fill="var(--teal)"/>
      <path d="M350 53 C342 44 343 34 350 33 C357 34 358 44 350 53 Z" fill="#fff"/>
      <circle cx="350" cy="39" r="2.5" fill="var(--teal)"/>
    </g>
    <!-- phone icon -->
    <g class="icon icon--phone">
      <circle cx="540" cy="140" r="18" fill="var(--teal)"/>
      <rect x="534" y="130" width="12" height="20" rx="2" fill="#fff"/>
      <rect x="536" y="133" width="8" height="12" fill="var(--teal)"/>
    </g>
    <!-- monitor icon -->
    <g class="icon icon--screen">
      <circle cx="100" cy="172" r="22" fill="none" stroke="#fff" stroke-width="2"/>
      <rect x="88" y="162" width="24" height="15" rx="1.5" fill="none" stroke="#fff" stroke-width="2"/>
      <path d="M96 183 H104 M100 177 V183" stroke="#fff" stroke-width="2"/>
    </g>
    <!-- social markers -->
    <circle cx="318" cy="259" r="13" fill="#fff"/>
    <circle cx="318" cy="297" r="13" fill="#fff"/>
    <circle cx="318" cy="335" r="13" fill="#fff"/>
  </svg>

  <p class="text holder__name">GARETH PEMBROKE</p>
  <p class="text holder__role">DIRECTOR</p>
  <p class="text address">214 9th Floor,<br>Harbour Lane NTH</p>
  <p class="text phone">0452 803716<br>0452 803716</p>
  <p class="text web">hello@mapleridgegroup.com<br>www.mapleridgegroup.com</p>
  <p class="text social social--one">community/mapleridge</p>
  <p class="text social social--two">updates/mapleridge</p>
  <p class="text social social--three">network/mapleridge</p>
</section>

</body>
</html>
```